Cleaning and Restoration Firm requires a Monthly Newsletter

I would like to begin a monthly newsletter. We have done them in the past, but they have not been professionally designed.

The website is www.brightholtcare.com.au
I have included a file nook link to use pictures, logo, etc
https://www.filetrove.net/sh/pq3m9tr2x81vbn4/QZXrTy7LmKdNe2Wf-Hpo-4sGj?dl=0

I have included some links to old newsletters, just for the ideas
http://email.pulvio.com.au/em/mail/view.php?id=2004417&a=51290&k=ab91f3e
http://email.pulvio.com.au/em/mail/view.php?id=2003862&a=51290&k=7d2e5c1
http://email.pulvio.com.au/em/mail/view.php?id=2003379&a=51290&k=e40b9a6
http://email.pulvio.com.au/em/mail/view.php?id=2002915&a=51290&k=9c8f174

We are introducing the new cleaning work vehicle and restoration work trailer. The work vehicle which has taken 5 months to build followed by another 5 months to completely fit out with the new custom built machine and equipment is a one of a kind unit, never been attempted before.

We can do a special of 10% off all carpet and upholstery cleaning jobs for the next 30 days, must be booked in the next 14 days to qualify. Including commercial jobs.

Reason: Looking for a unique design and idea. Looking for something fresh. HAVE INCREASED THE BUDGET

Target Market(s)

Everyone and anyone, tenants moving out of rentals, retirees and professionals looking after the home, spring cleans, emergency water and fire damage, mould remeedation, pre sale cleans,

Font styles to use
Sans Serif

Requirements
Must have
• I would like a fresh email newsletter that is informative, one that shows more info each month about the cleaning and restoration industry, offering clients plenty useful info without having to read too much.
• Professional template.
• An email and SMS return message that will make it easy for clients to book in a on site consultation or phone quote.
• A mingleboard add, like section
• and quotation or just a phone call for advice as this is needed for all restoration work.
• Also to find out a bit of info about us and link to the current and any future websites.
Nice to have
• Something new and fresh.
• Links, Visit our website, services, contact us, like us on mingleboard
Should not have
• Surprise me!

```html
<!DOCTYPE html>
<html lang="en">
<head>
<meta charset="utf-8">
<title>Brightholt Care Newsletter</title>
<link href="https://fonts.googleapis.com/css2?family=Open+Sans:wght@400;600;700;800&family=Roboto+Condensed:wght@400;700&display=swap" rel="stylesheet">
<style>
:root{
  --navy:#0b2350;
  --navy-dark:#071a3d;
  --blue:#1f5fd0;
  --blue-mid:#2a6fe0;
  --pink:#e8197d;
  --orange:#f7a21b;
  --orange-deep:#f08c0b;
  --cream:#fdf0d8;
  --white:#ffffff;
  --ink:#333a44;
}
*{margin:0;padding:0;box-sizing:border-box}
html,body{width:1200px;height:2792px;overflow:hidden;background:var(--white)}
body{font-family:"Open Sans",Arial,sans-serif;color:var(--ink);position:relative}
.section{position:absolute;left:0;width:1200px}

/* top nav */
.topnav{top:0;height:64px;background:var(--white);display:flex;justify-content:center;align-items:center;gap:18px;font-size:17px;color:#222}
.topnav span.sep{color:#888}

/* hero */
.hero{top:64px;height:380px;background:var(--cream)}
.hero-photo{position:absolute;left:40px;top:0;width:440px;height:360px;background:linear-gradient(160deg,#cfe3f2 0%,#e9eef2 45%,#8fa9bc 100%)}
.brand{position:absolute;left:620px;top:50px;display:flex;align-items:center;gap:18px}
.brand-mark{width:58px;height:58px;border-radius:50%;background:var(--blue)}
.brand-name{font-size:44px;font-weight:800;color:var(--navy)}
.badges{position:absolute;left:640px;top:150px;display:flex;gap:22px}
.badges div{width:64px;height:64px;background:#d8dfe9;border-radius:6px}
.badges div:nth-child(2){border-radius:50%}
.pills{position:absolute;left:250px;top:320px;display:flex}
.pill{height:64px;padding:0 32px;display:flex;align-items:center;font-size:32px;color:var(--white);border-radius:32px}
.pill.pink{background:var(--pink);position:relative;z-index:2}
.pill.blue{background:var(--blue);margin-left:-28px;padding-left:52px}

/* offer */
.offer{top:444px;height:500px;background:var(--navy)}
.offer-card{position:absolute;left:250px;top:0;width:700px;height:495px}
.offer-card svg{position:absolute;inset:0}
.offer-body{position:relative;text-align:center;padding-top:30px}
.offer-big{color:var(--pink);font-weight:800;font-size:112px;line-height:1;display:inline-flex;align-items:flex-start}
.offer-big small{font-size:50px;margin-top:42px}
.offer-text{width:560px;margin:20px auto 0;font-size:23px;line-height:1.35;color:#555}
.btn{display:inline-block;background:var(--orange);color:var(--white);font-weight:600;border-radius:8px}
.offer .btn{margin-top:20px;font-size:28px;padding:8px 32px}
.offer-or{font-size:26px;margin-top:10px;color:#333;line-height:1.3}
.offer-phone{font-size:50px;font-weight:700;color:#222;letter-spacing:2px;line-height:1.3}

/* vehicle */
.vehicle{top:944px;height:620px;background:var(--blue-mid)}
.vehicle h2{text-align:center;color:var(--white);font-weight:700;font-size:38px;line-height:1.35;padding-top:80px}
.vehicle-text{position:absolute;left:80px;top:300px;width:380px;height:210px;background:var(--navy);color:var(--white);font-size:18px;line-height:1.55;padding:20px 16px}
.vehicle-btns{position:absolute;left:90px;top:520px;display:flex;gap:20px}
.vehicle-btns .btn{font-size:19px;padding:8px 18px}
.vehicle-photo{position:absolute;left:520px;top:256px;width:600px;height:310px;background:var(--white);padding:14px}
.vehicle-photo div{width:100%;height:100%;background:linear-gradient(180deg,#9ec3e0 0%,#dde9f2 55%,#8f9aa4 100%)}

/* hotline */
.hotline{top:1564px;height:110px;background:var(--navy-dark);color:var(--white);text-align:center;font-family:"Roboto Condensed",Arial,sans-serif;font-weight:700;font-size:36px;line-height:110px}

/* columns */
.columns{top:1674px;height:620px;background:var(--navy)}
.col{position:absolute;top:16px;width:360px;height:570px}
.col svg.shape{position:absolute;inset:0}
.col-inner{position:relative;padding:24px 22px}
.col1{left:30px}.col2{left:420px}.col3{left:810px}
.col-head{font-family:"Roboto Condensed",Arial,sans-serif;font-weight:700;font-size:24px;color:var(--navy)}
.col1 .col-head{display:flex;gap:14px;align-items:center}
.icon-box{width:70px;height:70px;background:var(--navy);border-radius:4px;display:flex;align-items:center;justify-content:center}
.col1 ol{margin:40px 0 0 24px;font-size:17px;line-height:2;color:#333}
.col2 .col-head,.col3 .col-head{text-align:center;border-bottom:2px solid var(--navy);padding-bottom:12px}
.col2 p{text-align:center;font-size:17px;margin-top:18px;line-height:1.4;color:#333}
.seal{width:150px;height:150px;border-radius:50%;background:#5a8f3c;margin:28px auto 0}
.col3-photo{height:170px;margin-top:18px;background:linear-gradient(180deg,#6f6250 0%,#a89781 60%,#4d4336 100%)}
.col3 p{text-align:center;font-size:15px;margin-top:14px;line-height:1.45;color:#333}

/* services */
.services{top:2294px;height:360px;background:var(--white)}
.svc-water{position:absolute;left:40px;top:0;width:520px;height:232px;background:linear-gradient(160deg,#1a5fb0,#64a9e6)}
.svc-fire{position:absolute;left:40px;top:240px;width:256px;height:120px;background:linear-gradient(160deg,#b23a10,#f08a2a)}
.svc-mould{position:absolute;left:304px;top:240px;width:256px;height:120px;background:linear-gradient(160deg,#3b4f2a,#8b9a5e)}
.svc-label{position:absolute;left:16px;bottom:10px;color:var(--white);font-weight:800;font-size:30px}
.svc-fire .svc-label,.svc-mould .svc-label{font-size:20px}
.svc-list{position:absolute;left:570px;top:0;width:590px;height:360px;background:var(--cream)}
.svc-child{position:absolute;right:0;top:150px;width:240px;height:210px;background:linear-gradient(160deg,#f3d7c4,#e7b8a0)}
.svc-list ul{list-style:none;position:relative;padding:28px 0 0 30px;font-weight:700;font-size:36px;line-height:1.3;color:var(--pink)}
.svc-list li{display:flex;justify-content:space-between;width:380px;align-items:center}
.svc-list li::after{content:"";width:14px;height:14px;border-radius:50%;background:var(--pink)}

/* footer */
.footer{top:2654px;height:138px;background:var(--navy-dark);color:var(--white)}
.footer-call{position:absolute;left:70px;top:26px;text-align:center}
.footer-call .lead{color:var(--orange);font-size:30px}
.footer-call .nums{font-size:28px;font-weight:700;margin-top:4px}
.footer .btn{position:absolute;left:720px;top:46px;font-size:20px;padding:10px 26px;background:var(--orange-deep)}
</style>
</head>
<body>

<nav class="section topnav">
  <span>Visit Our Website</span><span class="sep">|</span>
  <span>Services</span><span class="sep">|</span>
  <span>Contact Us</span><span class="sep">|</span>
  <span>Send To A Friend</span><span class="sep">|</span>
  <span>Like Us On mingleboard</span>
</nav>

<header class="section hero">
  <div class="hero-photo" role="img" aria-label="Branded work van parked outside"></div>
  <div class="brand"><div class="brand-mark"></div><div class="brand-name">Brightholt Care</div></div>
  <div class="badges"><div></div><div></div><div></div><div></div></div>
  <div class="pills">
    <div class="pill pink">Professional Cleaners</div>
    <div class="pill blue">Professional Restorers</div>
  </div>
</header>

<section class="section offer">
  <div class="offer-card">
    <svg width="700" height="495" viewBox="0 0 700 495"><polygon points="0,0 700,0 700,440 350,495 0,440" fill="#fff"/></svg>
    <div class="offer-body">
      <div class="offer-big">10%<small>OFF</small></div>
      <p class="offer-text">All carpet and upholstery cleaning jobs for the next 30 days, must be booked in the next 14 days to qualify, including commercial jobs.</p>
      <span class="btn">BOOK NOW</span>
      <div class="offer-or">or call now</div>
      <div class="offer-phone">0491 552 307</div>
    </div>
  </div>
</section>

<section class="section vehicle">
  <h2>INTRODUCING THE NEW CLEANING WORK VEHICLE<br>&amp; RESTORATION WORK TRAILER</h2>
  <p class="vehicle-text">The work vehicle which has taken 5 months to build followed by another 5 months to completely fit out with the new custom built machine and equipment is a one of a kind unit, never been attempted before.....</p>
  <div class="vehicle-btns"><span class="btn">MORE INFO</span><span class="btn">BOOK NOW</span></div>
  <div class="vehicle-photo"><div role="img" aria-label="New restoration work trailer with branded livery"></div></div>
</section>

<div class="section hotline">24x7 SERVICES, PHONE 4071 8846, 0491 552 307</div>

<section class="section columns">
  <div class="col col1">
    <svg class="shape" width="360" height="570" viewBox="0 0 360 570"><polygon points="0,0 360,0 360,500 180,570 0,500" fill="#f7a21b"/></svg>
    <div class="col-inner">
      <div class="col-head">
        <div class="icon-box"><svg width="40" height="40" viewBox="0 0 40 40"><polyline points="6,21 16,31 34,9" fill="none" stroke="#f7a21b" stroke-width="6"/></svg></div>
        <span>REASON TO<br>CHOOSE US</span>
      </div>
      <ol>
        <li>Reputation</li><li>Experience</li><li>Education &amp; Certification</li>
        <li>Cleaning Systems</li><li>First Class Customer Service</li><li>100% Money Back Guarantee</li>
      </ol>
    </div>
  </div>
  <div class="col col2">
    <svg class="shape" width="360" height="570" viewBox="0 0 360 570"><polygon points="0,0 360,0 360,500 180,570 0,500" fill="#f7a21b"/></svg>
    <div class="col-inner">
      <div class="col-head">OUR GUARENTEE TO YOU</div>
      <p>The Healthiest, Cleanest, Freshest Carpet &amp; Upholstery Cleaning possible</p>
      <div class="seal"></div>
    </div>
  </div>
  <div class="col col3">
    <svg class="shape" width="360" height="570" viewBox="0 0 360 570"><polygon points="0,0 360,0 360,500 180,570 0,500" fill="#f7a21b"/></svg>
    <div class="col-inner">
      <div class="col-head">COMMERCIAL SERVICE</div>
      <div class="col3-photo" role="img" aria-label="Freshly cleaned commercial carpet in an office"></div>
      <p>Recognised as the expert in the top three most sought out restoration procedures, Brightholt Care will select the best fit for your company or business, explain the benefits and tailor a program that maximises your flooring maintenance budget.</p>
    </div>
  </div>
</section>

<section class="section services">
  <div class="svc-water" role="img" aria-label="Water splash for water restoration"><span class="svc-label">WATER RESTORATION</span></div>
  <div class="svc-fire" role="img" aria-label="Flames for fire restoration"><span class="svc-label">FIRE RESTORATION</span></div>
  <div class="svc-mould" role="img" aria-label="Mould growth for mould remediation"><span class="svc-label">MOLD REMEDIATION</span></div>
  <div class="svc-list">
    <div class="svc-child" role="img" aria-label="Child relaxing on a clean carpet"></div>
    <ul>
      <li>Pest Management</li><li>Water Damage</li><li>Fire Damage</li>
      <li>Carpet and Rug</li><li>Tile and Grout</li><li>Upholstery</li>
    </ul>
  </div>
</section>

<footer class="section footer">
  <div class="footer-call">
    <div class="lead">Call Us or Book Now</div>
    <div class="nums">PHONE 4071 8846, 0491 552 307</div>
  </div>
  <span class="btn">BOOK YOUR CLEANING SCHEDULE NOW</span>
</footer>

</body>
</html>
```